Business Card for Business consulting practice

Need a design for a consultant business card. Simple and elegant.
I need the following information on the card:
Logo: (see uploaded file)
Company name: Calmora Advisory Group
Name: Dana Weltrup
Title: Managing Director - Aerospace and Defence
Phone #: 514-268-3917
e-mail: dana.weltrup@calmora-example.com
Website: www.calmora-example.com
Tagline: Proposals Management and Capture support for complex procurements

```html
<!DOCTYPE html>
<html lang="en">
<head>
<meta charset="utf-8">
<title>Calmora Advisory Group – Business Card</title>
<link href="https://fonts.googleapis.com/css2?family=Libre+Baskerville:wght@400;700&family=Montserrat:wght@400;500&display=swap" rel="stylesheet">
<style>
  :root {
    --page-bg: #d9dadb;
    --navy-deep: #172536;
    --navy-mid: #23394f;
    --steel-blue: #3f7aa8;
    --pill-blue: #4a8dbf;
    --sky-text: #5b9cd0;
    --paper: #ffffff;
    --ink-navy: #1b2b3d;
    --soft-white: #e9eef3;
  }
  * { margin: 0; padding: 0; box-sizing: border-box; }
  html, body { width: 1200px; height: 857px; overflow: hidden; }
  body {
    background: var(--page-bg);
    font-family: "Montserrat", sans-serif;
    position: relative;
  }
  .card {
    position: absolute;
    width: 525px;
    height: 300px;
    overflow: hidden;
    border-radius: 3px;
    box-shadow: 0 14px 30px rgba(0,0,0,0.22);
  }

  /* Front */
  .card-front { left: 60px; top: 100px; background: var(--paper); }
  .front-lower {
    position: absolute; left: 0; right: 0; bottom: 0; height: 140px;
    background: linear-gradient(110deg, var(--navy-deep) 0%, var(--navy-mid) 60%, var(--steel-blue) 100%);
  }
  .brand {
    position: absolute; left: 0; right: 0; top: 44px;
    display: flex; align-items: center; justify-content: center; gap: 12px;
  }
  .brand-dot { width: 18px; height: 18px; border-radius: 50%; background: var(--steel-blue); }
  .brand-name {
    font-family: "Libre Baskerville", serif; font-weight: 700;
    font-size: 27px; letter-spacing: 1px; color: var(--ink-navy);
  }
  .card-back .brand-name { color: var(--soft-white); }
  .brand-rule {
    position: absolute; left: 90px; right: 90px; top: 96px;
    height: 1.5px; background: var(--steel-blue);
  }
  .tagline-pill {
    position: absolute; left: 88px; top: 130px; width: 300px;
    padding: 9px 16px; border-radius: 10px;
    background: var(--pill-blue); color: var(--paper);
    font-family: "Libre Baskerville", serif; font-weight: 700;
    font-size: 13px; line-height: 1.3; text-align: center;
  }
  .person { position: absolute; left: 34px; bottom: 36px; }
  .person-name {
    font-family: "Libre Baskerville", serif; font-weight: 700;
    font-size: 14px; color: var(--paper); text-transform: uppercase; margin-bottom: 6px;
  }
  .person-title { font-size: 11.5px; color: var(--sky-text); line-height: 1.35; }
  .contact-list {
    position: absolute; right: 22px; top: 196px; list-style: none;
  }
  .contact-list li {
    display: flex; align-items: center; justify-content: flex-end; gap: 10px;
    font-size: 11.5px; color: var(--paper); height: 24px;
  }
  .contact-icon {
    width: 18px; height: 18px; border-radius: 50%; background: var(--pill-blue);
    display: flex; align-items: center; justify-content: center;
  }

  /* Back */
  .card-back {
    left: 615px; top: 455px;
    background: linear-gradient(150deg, var(--navy-deep) 0%, var(--navy-mid) 55%, var(--steel-blue) 100%);
  }
  .card-back .brand { top: 96px; }
  .card-back .brand-rule { top: 148px; left: 100px; right: 100px; }
  .back-tagline {
    position: absolute; left: 0; right: 0; top: 166px; text-align: center;
    font-family: "Libre Baskerville", serif; font-size: 13px; line-height: 1.4;
    color: var(--soft-white);
  }
</style>
</head>
<body>

  <section class="card card-front">
    <div class="front-lower"></div>
    <div class="brand">
      <span class="brand-dot"></span>
      <span class="brand-name">Calmora Advisory Group</span>
    </div>
    <div class="brand-rule"></div>
    <p class="tagline-pill">Proposals Management and Capture support for complex procurements</p>
    <div class="person">
      <p class="person-name">Dana Weltrup</p>
      <p class="person-title">Managing Director<br>Aerospace and Defence</p>
    </div>
    <ul class="contact-list">
      <li>514-268-3917
        <span class="contact-icon"><svg width="10" height="10" viewBox="0 0 24 24"><path fill="#fff" d="M6.6 10.8a15 15 0 0 0 6.6 6.6l2.2-2.2c.3-.3.7-.4 1-.2 1.1.4 2.3.6 3.6.6.6 0 1 .4 1 1V20c0 .6-.4 1-1 1A17 17 0 0 1 3 4c0-.6.4-1 1-1h3.5c.6 0 1 .4 1 1 0 1.3.2 2.5.6 3.6.1.3 0 .7-.2 1z"/></svg></span>
      </li>
      <li>dana.weltrup@calmora-example.com
        <span class="contact-icon"><svg width="10" height="10" viewBox="0 0 24 24"><rect x="2" y="5" width="20" height="14" rx="1" fill="none" stroke="#fff" stroke-width="2.2"/><path d="M2 6l10 7 10-7" fill="none" stroke="#fff" stroke-width="2.2"/></svg></span>
      </li>
      <li>www.calmora-example.com
        <span class="contact-icon"><svg width="10" height="10" viewBox="0 0 24 24"><g fill="none" stroke="#fff" stroke-width="2"><circle cx="12" cy="12" r="10"/><ellipse cx="12" cy="12" rx="4" ry="10"/><path d="M2 12h20"/></g></svg></span>
      </li>
    </ul>
  </section>

  <section class="card card-back">
    <div class="brand">
      <span class="brand-dot"></span>
      <span class="brand-name">Calmora Advisory Group</span>
    </div>
    <div class="brand-rule"></div>
    <p class="back-tagline">Proposals Management and Capture support<br>for complex procurements</p>
  </section>

</body>
</html>
```